Birchfield Vacation Rentals Bill Board

7x21 bill board.

Im needing a bill board for a vacation rental company. Specializing in cabin rentals.
Here are the main points I want mentioned on the billboard:

Quality vacation rentals

Accepting new vacation rental homes.

Family owned and operated.

Birchfieldvr.example
555-318-7042

Use either logo whichever looks best. Be creative

Target Market(s)

Cabin owners

Industry/Entity Type

Hospitality

Font styles to use
Sans Serif

Requirements
Must have
• Would like the cabin picture to be the background. Must have the birchfield logo, phone number and website

```html
<!DOCTYPE html>
<html lang="en">
<head>
<meta charset="utf-8">
<title>Birchfield Vacation Rentals Billboard</title>
<link href="https://fonts.googleapis.com/css2?family=Archivo+Black&family=Montserrat:wght@600;700&display=swap" rel="stylesheet">
<style>
  :root {
    --page: #dfe7ee;
    --cream: #f8e5b0;
    --amber: #b87400;
    --bark: #6b3a08;
    --copper: #9a5c00;
    --white: #ffffff;
  }
  * { margin: 0; padding: 0; box-sizing: border-box; }
  html, body { width: 1200px; height: 900px; overflow: hidden; }
  body { background: var(--page); position: relative; font-family: "Montserrat", sans-serif; }

  .billboard {
    position: absolute;
    left: 0; top: 300px;
    width: 1200px; height: 300px;
    overflow: hidden;
    background: var(--cream);
  }
  .billboard-art { position: absolute; inset: 0; width: 1200px; height: 300px; }

  .headline {
    position: absolute;
    left: 0; width: 760px;
    text-align: center;
    font-family: "Archivo Black", sans-serif;
    font-weight: 400;
    color: var(--bark);
    -webkit-text-stroke: 5px var(--white);
    paint-order: stroke fill;
    line-height: 1;
    white-space: nowrap;
  }
  .headline-top { top: 16px; font-size: 64px; letter-spacing: 0.5px; }
  .headline-bottom { top: 80px; font-size: 64px; letter-spacing: 1px; }

  .offer-pill {
    position: absolute;
    left: 114px; top: 150px;
    width: 528px; height: 35px;
    background: var(--amber);
    border-radius: 10px;
    color: var(--white);
    font-weight: 700;
    font-size: 21px;
    line-height: 35px;
    text-align: center;
    letter-spacing: 0.2px;
    white-space: nowrap;
  }

  .tagline {
    position: absolute;
    left: 0; width: 760px; top: 195px;
    text-align: center;
    color: var(--copper);
    font-weight: 700;
    font-size: 22px;
    letter-spacing: 0.4px;
    white-space: nowrap;
  }

  .brand-name {
    position: absolute;
    left: 20px; top: 245px;
    width: 210px;
    color: var(--white);
    font-weight: 600;
    font-size: 14px;
    line-height: 1.15;
    letter-spacing: 1.5px;
    text-transform: uppercase;
    text-align: center;
  }

  .contact {
    position: absolute;
    top: 264px;
    color: var(--white);
    font-weight: 700;
    font-size: 21px;
    line-height: 30px;
    letter-spacing: 0.2px;
    white-space: nowrap;
  }
  .contact-web { left: 300px; }
  .contact-phone { left: 580px; }
</style>
</head>
<body>
  <section class="billboard">
    <svg class="billboard-art" viewBox="0 0 1200 300">
      <defs>
        <linearGradient id="cabin-tones" x1="0" y1="0" x2="0" y2="1">
          <stop offset="0" stop-color="#d9a3c6"/>
          <stop offset="0.25" stop-color="#f2b46a"/>
          <stop offset="0.5" stop-color="#b8682a"/>
          <stop offset="0.8" stop-color="#7a5236"/>
          <stop offset="1" stop-color="#b49a78"/>
        </linearGradient>
      </defs>
      <path class="contact-band" d="M0 237 H233 L247 260 H860 L880 300 H0 Z" fill="var(--amber)"/>
      <path class="photo-crescent" d="M800 0 C700 70 700 230 830 300 H1200 V0 Z" fill="var(--amber)"/>
      <path class="cabin-photo" d="M816 0 C735 75 735 225 845 300 H1200 V0 Z" fill="url(#cabin-tones)" role="img" aria-label="Photo of a large wooden mountain cabin with wraparound decks at sunset"/>
    </svg>

    <h1 class="headline headline-top">Quality Vacation</h1>
    <h1 class="headline headline-bottom">RENTALS</h1>

    <p class="offer-pill">Accepting New Vacation Rental Homes</p>
    <p class="tagline">Family Owned and Operated</p>

    <p class="brand-name">Birchfield<br>Vacation Rentals</p>

    <p class="contact contact-web">Birchfieldvr.example</p>
    <p class="contact contact-phone">555-318-7042</p>
  </section>
</body>
</html>
```